Brisk Therapy Flyer - Physiotherapy company

I am looking for a two-sided flyer (4"x8") that can be easily posted on cork boards or displayed as needed to provide information about my business. I would like to use the colors found in my logo (see attached) along with white and black. Please have a look at my website for ideas of how I would like the color schemes etc (www.briskcare-demo.ca). I would like it to follow the same style as my website.<br/><br/>FRONT SIDE<br/>I am hoping to have the name of our business "Brisk Therapy" with our slogan "Boreal Physiotherapy - Rehab and Recovery Above the Pines (degrees symbol)" underneath. Somewhere above or around this I would like my logo (see attached). <br/><br/>Below that I would like a title "Services Provided" and then listed: <br/>Mobile Services<br/>Clinic<br/>Telehealth<br/><br/>Below that, I would like another title "Treatments Offered" and then listed: <br/>Hands-on manual therapy<br/>Intramuscular Stimulation (IMS)<br/>Acupuncture<br/>Athletic taping<br/>Injury/condition education<br/>Supervised exercise<br/><br/>Below that I would like "Contact Us":<br/>Brisk Therapy<br/>www.BriskCare-demo.ca<br/>Book online through https://briskcare.bookfake-demo.com/<br/>physio@briskcare-demo.ca<br/>867-555-0148<br/>Direct Billing offered for most extended health providers<br/>(Chatterly, Snapwell logo, kinelogix logo (see attached) on bottom maybe in corner or centered)<br/><br/>BACK SIDE<br/><br/>I would like the logo on there once again maybe. Then I would like these three information sections one on top of the other spaced out appropriately.<br/><br/>Image (needling image) (see attached)<br/>Title: Mobile Physiotherapy<br/>The information below title: If you want to keep moving and need some help, but your current condition makes it difficult or unsafe to travel to and from a clinic to see a physiotherapist, that’s where we come in. We make it easy by offering a mobile service that provides exceptional one-on-one physiotherapy assessment and treatment in the comfort of your own home. There is a small fee to access mobile services. <br/><br/>Image (Hands on knee image) (see attached)<br/>Title: Clinic<br/>The information below title: If you have an injury that is causing you pain or restricting you from doing the activities that you want to do then physiotherapy can help. A traditional approach to physiotherapy where you come to our clinic and we provide one to one education and hands on therapy. <br/><br/>Image (computer, tablet etc) (see attached)<br/>Title: Telehealth<br/>The information below title: If you live outside of Whitehorse or just want easy access to a physiotherapist from the comfort of your home, then Telehealth is for you. Telehealth involves meeting with your physiotherapist using real-time technology, similar to VidLink. Brisk Therapy utilizes Kinelogix for exercise prescription, pain tracking and telehealth. Through Kinelogix or it’s Motivapp you can discuss your treatment plan, diagnoses, exercises, daily activities or any other questions you may have directly with a physiotherapist.<br/><br/><br/><br/>

Industry/Entity Type

Healthcare

Colors

Designer to choose colors to be used in the design.

Requirements
Must have
• Follow the same colors and schemes of my website (www.briskcare-demo.ca)
• Keep it clean and concise
Nice to have
• Images might not fit because I don't want it too cluttered.
Should not have
• Too busy

```html
<!DOCTYPE html>
<html lang="en">
<head>
<meta charset="utf-8">
<title>Brisk Therapy – Services Flyer</title>
<link rel="stylesheet" href="https://fonts.googleapis.com/css2?family=Roboto+Slab:wght@300;400;700&family=Roboto:wght@700&display=swap">
<style>
  :root {
    --navy-deep: #16254a;
    --navy-mid: #1f3866;
    --navy-glow: #2d5488;
    --title-blue: #2a416f;
    --silver-light: #f4f5f7;
    --silver-dark: #a9adb3;
    --forest: #155a4b;
    --grey-band: #b3b6ba;
    --muted-text: #8a8d91;
    --white: #ffffff;
  }
  * { margin: 0; padding: 0; box-sizing: border-box; }
  html, body { width: 1200px; height: 2400px; overflow: hidden; }
  body { font-family: "Roboto Slab", Georgia, serif; }

  .flyer {
    position: relative;
    width: 1200px;
    height: 2400px;
    overflow: hidden;
    background: radial-gradient(ellipse 70% 45% at 50% 82%, var(--navy-glow) 0%, var(--navy-mid) 45%, var(--navy-deep) 100%);
  }

  .section-title {
    position: absolute;
    left: 88px;
    height: 78px;
    background: linear-gradient(90deg, var(--silver-dark) 0%, var(--silver-light) 35%, var(--silver-light) 65%, var(--silver-dark) 100%);
    clip-path: polygon(0 0, calc(100% - 50px) 0, 100% 100%, 0 100%);
    box-shadow: 0 10px 16px rgba(0,0,0,.35);
    color: var(--title-blue);
    font-weight: 700;
    font-size: 44px;
    line-height: 78px;
    padding-left: 32px;
    letter-spacing: .3px;
    white-space: nowrap;
  }
  .title-mobile { top: 95px; width: 647px; }
  .title-clinic { top: 700px; width: 367px; padding-left: 35px; }
  .title-telehealth { top: 1182px; width: 377px; padding-left: 20px; }

  .body-copy {
    position: absolute;
    left: 92px;
    color: var(--white);
    font-weight: 300;
    font-size: 32px;
    line-height: 41.7px;
    white-space: nowrap;
  }
  .copy-mobile { top: 213px; }
  .copy-clinic { top: 812px; left: 94px; }
  .copy-telehealth { top: 1287px; }

  .photo-circle {
    position: absolute;
    border-radius: 50%;
    border: 10px solid #cfd2d6;
    box-shadow: 0 0 0 2px #8f949a, 0 12px 24px rgba(0,0,0,.35);
  }
  .photo-needling {
    left: 688px; top: 157px; width: 425px; height: 425px;
    background: radial-gradient(circle at 60% 55%, #e6c3ad 0%, #d8ad94 35%, #eef0f2 75%);
  }
  .photo-knee {
    left: 683px; top: 726px; width: 425px; height: 425px;
    background: radial-gradient(circle at 50% 45%, #c08f74 0%, #8c6250 35%, #3a3a3d 75%);
  }
  .device-visual {
    position: absolute;
    left: 436px; top: 1270px; width: 672px; height: 326px;
    border-radius: 16px;
    background: linear-gradient(180deg, #f2f3f5 0%, #dfe2e6 70%, #bfc3c8 100%);
  }

  .footer-bands { position: absolute; left: 0; top: 1900px; }

  .brand-name {
    position: absolute;
    left: 40px; top: 2262px;
    width: 320px;
    text-align: center;
    color: var(--forest);
    font-weight: 700;
    font-size: 40px;
    line-height: 50px;
    white-space: nowrap;
  }

  .footer-divider {
    position: absolute;
    left: 374px; top: 2085px;
    width: 2px; height: 275px;
    background: #e2e3e5;
  }
  .footer-tagline {
    position: absolute;
    left: 403px; top: 2102px;
    color: var(--muted-text);
    font-weight: 400;
    font-size: 28px;
    line-height: 40.5px;
  }
  .footer-web {
    position: absolute;
    left: 403px; top: 2234px;
    color: var(--forest);
    font-weight: 700;
    font-size: 37px;
    white-space: nowrap;
  }
  .footer-phone {
    position: absolute;
    left: 402px; top: 2274px;
    color: var(--forest);
    font-family: "Roboto", Arial, sans-serif;
    font-weight: 700;
    font-size: 74px;
    letter-spacing: -1px;
    white-space: nowrap;
  }
</style>
</head>
<body>
<main class="flyer">

  <h2 class="section-title title-mobile">MOBILE PHYSIOTHERAPY</h2>
  <div class="photo-circle photo-needling" role="img" aria-label="Photo of a physiotherapist applying acupuncture needles to a patient's shoulder"></div>
  <p class="body-copy copy-mobile">
    &nbsp;If you want to keep moving and<br>
    need some help, but your current<br>
    condition makes it difficult or<br>
    unsafe to travel to and from a<br>
    clinic to see a physiotherapist,<br>
    that’s where we come in. We make<br>
    it easy by offering a mobile service<br>
    that provides exceptional one-on-<br>
    one physiotherapy assessment and<br>
    treatment in the comfort of your own<br>
    home. There is a small fee to access mobile services.
  </p>

  <h2 class="section-title title-clinic">CLINIC</h2>
  <div class="photo-circle photo-knee" role="img" aria-label="Photo of a therapist's hands working on a patient's knee"></div>
  <p class="body-copy copy-clinic">
    If you have an injury that is causing<br>
    you pain or restricting you from<br>
    doing the activities that you want<br>
    to do then physiotherapy can<br>
    help. A traditional approach to<br>
    physiotherapy where you come to<br>
    our clinic and we provide one to one<br>
    education and hands on therapy.
  </p>

  <h2 class="section-title title-telehealth">TELEHEALTH</h2>
  <div class="device-visual" role="img" aria-label="Laptop, tablet, phone and watch showing the exercise and video call app"></div>
  <p class="body-copy copy-telehealth">
    If you live outside of<br>
    Whitehorse or just<br>
    want easy access to<br>
    a physiotherapist<br>
    from the comfort<br>
    of your home, then<br>
    Telehealth is for you.<br>
    Telehealth involves<br>
    meeting with your physiotherapist using real-time technology,<br>
    similar to VidLink. Brisk Therapy utilizes Kinelogix for<br>
    exercise prescription, pain tracking and telehealth. Through<br>
    Kinelogix or it’s Motivapp you can discuss your treatment plan,<br>
    diagnoses, exercises, daily activities or any other questions you<br>
    may have directly with a physiotherapist.
  </p>

  <svg class="footer-bands" width="1200" height="500" viewBox="0 1900 1200 500" aria-hidden="true">
    <polygon points="0,2120 342,1908 1200,2290 1200,2400 0,2400" fill="var(--grey-band)"/>
    <polygon points="0,2150 342,1925 1200,2300 1200,2400 0,2400" fill="var(--forest)"/>
    <polygon points="0,2205 340,1968 1200,2345 1200,2400 0,2400" fill="var(--white)"/>
  </svg>

  <p class="brand-name">Brisk Therapy</p>

  <div class="footer-divider"></div>
  <p class="footer-tagline">Mobile in home<br>Physiotherapy for<br>Whitehorse, Yukon</p>
  <p class="footer-web">www.BriskCare-demo.ca</p>
  <p class="footer-phone">867-555-0148</p>

</main>
</body>
</html>
```